Indoor Air Restoration company needs graphic design for a 6x12 v nose trailer to wrap

We offer mold services, duct cleaning, water damage clean up and odor removal. "We find, fix and prevent mold, odor and allergen problems" is what we want to communicate on this trailer, which is a rolling billboard. We like the blue and orange color themes, as found in our logo. The company name is Brightwell Dwelling Partners and the logo is attached below. We'd like to see our message clearly, company name and what we offer. We tend to lean towards white letters on a darker background (blue or orange) but are very open to outside ideas, as we are stuck! Our website is available for reference if that is helpful. www.brightwelldwellnx.com The phone number to be printed on truck is 555-619-4027, Happy designing!!

Target Market(s)

Home owners

Industry/Entity Type

Indoor Air Quality, Mold Remediation

Font styles to use
Sans Serif

Colors
0054AA
0677BA
7BADD7
CADEEF
E8F1F8
F0912C
F2A743
F7CA91
FBE8D2
FDF5EE

Requirements
Must have
• our message, company name and phone
Nice to have
• services we offer (mold remediation, duct cleaning, water damage and odor removal
Should not have
• cartoon feel

```html
<!DOCTYPE html>
<html lang="en">
<head>
<meta charset="utf-8">
<title>Brightwell Dwelling Partners – Trailer Wrap</title>
<link href="https://fonts.googleapis.com/css2?family=Oswald:wght@600&family=Signika:wght@600&family=Ubuntu:wght@700&family=Patrick+Hand&display=swap" rel="stylesheet">
<style>
  :root {
    --page: #ffffff;
    --panel: #ebebf5;
    --navy: #2b2766;
    --service: #2f2c8e;
    --amber: #f9b51b;
    --amber-line: #f0912c;
    --ink: #1f1d1e;
    --highlight: #f3e236;
    --brand-blue: #0677ba;
    --wall-dark: #8b8690;
    --wall-light: #d9d6dc;
    --suit: #f4f4f7;
  }
  html, body {
    margin: 0;
    width: 848px;
    height: 1200px;
    overflow: hidden;
    background: var(--page);
  }
  .wrap-panel {
    position: absolute;
    left: 74px;
    top: 168px;
    width: 707px;
    height: 353px;
    background: var(--panel);
    border: 1px solid #000;
    box-sizing: border-box;
    overflow: hidden;
  }
  .hero-photo {
    position: absolute;
    left: 0;
    top: 0;
    width: 450px;
    height: 285px;
    background:
      radial-gradient(ellipse at 78% 45%, var(--suit) 0 22%, transparent 40%),
      linear-gradient(90deg, var(--wall-dark) 0%, var(--wall-light) 35%, var(--wall-dark) 60%, rgba(235,235,245,0) 100%);
    opacity: .9;
  }
  .wave-shapes {
    position: absolute;
    inset: 0;
    width: 707px;
    height: 353px;
  }
  .brand-mark {
    position: absolute;
    left: 105px;
    top: 72px;
    display: flex;
    align-items: center;
    gap: 6px;
    font-family: "Signika", sans-serif;
    font-weight: 600;
    font-size: 15px;
    color: var(--brand-blue);
  }
  .brand-mark .square {
    width: 14px;
    height: 14px;
    background: var(--brand-blue);
  }
  .company-name {
    position: absolute;
    left: 30px;
    width: 290px;
    top: 118px;
    margin: 0;
    text-align: center;
    font-family: "Oswald", sans-serif;
    font-weight: 600;
    color: var(--ink);
    line-height: 1;
    text-shadow: 0 0 6px #fff, 0 0 3px #fff;
  }
  .company-name .line-1 { display: block; font-size: 34px; letter-spacing: .5px; }
  .company-name .line-2 { display: block; font-size: 26px; margin-top: 2px; }
  .tagline {
    position: absolute;
    left: 45px;
    top: 200px;
    width: 270px;
    margin: 0;
    padding: 4px 6px;
    text-align: center;
    font-family: "Patrick Hand", sans-serif;
    font-size: 19px;
    line-height: 1.3;
    color: var(--ink);
    background: var(--highlight);
    transform: rotate(-2deg);
  }
  .services {
    position: absolute;
    left: 425px;
    top: 60px;
    font-family: "Signika", sans-serif;
    font-weight: 600;
    color: var(--service);
  }
  .services h2 {
    margin: 0 0 10px;
    font-size: 25px;
    font-weight: 600;
    text-decoration: underline;
    text-underline-offset: 3px;
  }
  .services ul {
    list-style: none;
    margin: 0;
    padding: 0;
    font-size: 27px;
    line-height: 37px;
  }
  .services li::before { content: "·"; }
  .phone {
    position: absolute;
    left: 25px;
    top: 288px;
    display: flex;
    align-items: center;
    gap: 10px;
    font-family: "Ubuntu", sans-serif;
    font-weight: 700;
    font-size: 34px;
    color: var(--ink);
    letter-spacing: 1px;
  }
  .phone-icon {
    width: 38px;
    height: 38px;
  }
</style>
</head>
<body>
  <section class="wrap-panel">
    <div class="hero-photo" role="img" aria-label="Moldy wall with a technician in white protective suit, goggles and respirator holding a yellow pump sprayer"></div>

    <svg class="wave-shapes" viewBox="0 0 707 353" aria-hidden="true">
      <path d="M325 0 C400 18 480 28 560 34 C640 40 690 46 707 52 L707 0 Z" fill="var(--navy)" stroke="var(--amber-line)" stroke-width="1.5"/>
      <path d="M0 262 C180 290 380 250 560 258 C640 262 690 296 707 318 L707 353 L0 353 Z" fill="var(--amber)" stroke="var(--navy)" stroke-width="2"/>
    </svg>

    <div class="brand-mark"><span class="square"></span>Brightwell Dwelling Partners</div>

    <h1 class="company-name">
      <span class="line-1">BRIGHTWELL</span>
      <span class="line-2">DWELLING PARTNERS</span>
    </h1>

    <p class="tagline">We find, fix and prevent mold,<br>odor and allergen problems</p>

    <div class="services">
      <h2>Our services:</h2>
      <ul>
        <li>Mold Remediation</li>
        <li>Duct Cleaning</li>
        <li>Water Damage</li>
        <li>Odor Removal</li>
      </ul>
    </div>

    <div class="phone">
      <svg class="phone-icon" viewBox="0 0 38 38" aria-hidden="true">
        <defs>
          <linearGradient id="icon-metal" x1="0" y1="0" x2="1" y2="1">
            <stop offset="0" stop-color="#f2f2f2"/>
            <stop offset="1" stop-color="#9a9a9a"/>
          </linearGradient>
        </defs>
        <rect x="1" y="1" width="36" height="36" rx="5" fill="url(#icon-metal)" stroke="#8a8a8a"/>
        <path d="M16 10 h4 v5 h-3 c-1 3 -1 6 0 9 h3 v5 h-4 c-4 -5 -4 -14 0 -19 z" fill="#555"/>
      </svg>
      <span>555-619-4027</span>
    </div>
  </section>
</body>
</html>
```